Modern business card for triathlon training business in Australia

We need a business card design for our triathlon training company.

Pace with Us Fitness is an Australian business, owned by women, run for women. Pace with Us Fitness helps women prepare or improve triathlon skills and confidence through triathlon camps completely designed for women.

Our camps focus on preparing women both physically and mentally for their next (or first!) triathlon.

You can see our website www.pacewithusfitness.com.au for more info about our business and our style.

We've attached two of our logos and are happy to consider a design that utilised either colour scheme with the teal colour being our 'feature' colour. We don't want overly feminine cards but rather cards that are professional and neat. If the inclusion of any pictures/art is warranted, this should be focused on our swim/ride/run theme and in that specific order (swim/ride/run).

The business card needs to be a printable design and the contact details will need to change for our two employees.

Target Market(s)

Female clients and partners/vendors/sponsors that we work with in the triathlon industry

Industry/Entity Type

Fitness

Contact Information for Business Card

Pace with Us Fitness (business name)
Nina Carver
Business Director
Mobile: 0438 916 207
Email: nina@pacewithusfitness.com.au
www.pacewithusfitness.com.au

Second business card:
Pace with Us Fitness
Bel Stray
Coaching Director
Mobile: 0459 260 718
Email: bel@pacewithusfitness.com.au

Font styles to use
Serif
Sans Serif

Requirements
Must have
• Core contact details above, our logo and be a printable design
Should not have
• Pink
• Cursive/script fonts

```html
<!DOCTYPE html>
<html lang="en">
<head>
<meta charset="utf-8">
<title>Pace with Us Fitness — Business Card</title>
<link href="https://fonts.googleapis.com/css2?family=Varela+Round&family=Quicksand:wght@500;600&display=swap" rel="stylesheet">
<style>
  :root {
    --teal: #1fa7c1;
    --white: #ffffff;
    --backdrop: #ecefef;
  }
  * { margin: 0; padding: 0; box-sizing: border-box; }
  html, body {
    width: 1200px; height: 960px; overflow: hidden;
    background: var(--backdrop);
  }
  .business-card {
    position: absolute; left: 60px; top: 170px;
    width: 1080px; height: 620px;
    background: var(--teal);
    color: var(--white);
    overflow: hidden;
    box-shadow: 0 6px 18px rgba(0,0,0,.18);
  }
  .brand-name {
    position: absolute; left: 84px; top: 250px; width: 360px;
    font-family: "Varela Round", sans-serif;
    font-size: 50px; line-height: 1.08;
    text-transform: uppercase; letter-spacing: -0.5px;
  }
  .divider {
    position: absolute; left: 505px; top: 70px;
    width: 3px; height: 460px; background: var(--white);
  }
  .person-name {
    position: absolute; left: 592px; top: 66px;
    font-family: "Varela Round", sans-serif;
    font-size: 76px; letter-spacing: -2px; line-height: 1;
  }
  .person-title {
    position: absolute; right: 70px; top: 158px;
    font-family: "Quicksand", sans-serif; font-weight: 500;
    font-size: 26px; letter-spacing: 3px; text-transform: uppercase;
  }
  .contact-list {
    position: absolute; left: 540px; top: 228px; width: 490px;
    list-style: none; text-align: center;
    font-family: "Quicksand", sans-serif; font-weight: 500;
  }
  .contact-item { margin-bottom: 16px; }
  .contact-icon { display: block; margin: 0 auto 6px; }
  .contact-phone { font-size: 34px; letter-spacing: 3px; }
  .contact-text { font-size: 20px; letter-spacing: 2.6px; text-transform: uppercase; }
  .footer-bands { position: absolute; left: 0; bottom: 0; }
</style>
</head>
<body>
  <article class="business-card">
    <div class="brand-name">Pace with Us Fitness</div>

    <div class="divider"></div>

    <h1 class="person-name">Nina Carver</h1>
    <p class="person-title">Business Director</p>

    <ul class="contact-list">
      <li class="contact-item">
        <svg class="contact-icon" width="36" height="36" viewBox="0 0 36 36" aria-hidden="true">
          <path d="M3 12c0-6 30-6 30 0v4h-8v-4H11v4H3z" fill="#fff"/>
          <path d="M10 17h16l4 14H6z" fill="#fff"/>
          <g fill="#1fa7c1">
            <rect x="12" y="20" width="3" height="2.5"/><rect x="16.5" y="20" width="3" height="2.5"/><rect x="21" y="20" width="3" height="2.5"/>
            <rect x="11.5" y="24" width="3" height="2.5"/><rect x="16.5" y="24" width="3" height="2.5"/><rect x="21.5" y="24" width="3" height="2.5"/>
          </g>
        </svg>
        <span class="contact-phone">0438 916 207</span>
      </li>
      <li class="contact-item">
        <svg class="contact-icon" width="38" height="26" viewBox="0 0 38 26" aria-hidden="true">
          <rect x="1" y="1" width="36" height="24" fill="#fff"/>
          <path d="M1 1l18 13L37 1M1 25l13-12M37 25L24 13" stroke="#1fa7c1" stroke-width="2" fill="none"/>
        </svg>
        <span class="contact-text">nina@pacewithusfitness.com.au</span>
      </li>
      <li class="contact-item">
        <svg class="contact-icon" width="36" height="36" viewBox="0 0 36 36" aria-hidden="true">
          <g stroke="#fff" stroke-width="2.4" fill="none">
            <circle cx="18" cy="18" r="15"/>
            <ellipse cx="18" cy="18" rx="7" ry="15"/>
            <path d="M3 18h30M5.5 10h25M5.5 26h25"/>
          </g>
        </svg>
        <span class="contact-text">www.pacewithusfitness.com.au</span>
      </li>
    </ul>

    <svg class="footer-bands" width="1080" height="160" viewBox="0 0 1080 160" aria-hidden="true">
      <polygon points="0,70 830,28 870,80 0,125" fill="#fff"/>
      <polygon points="905,14 1080,4 1080,62 945,68" fill="#fff"/>
    </svg>
  </article>
</body>
</html>
```